Email Signature

We would like to have an email Signature designed.
We have an idea, and a logo that we would like to be make more professional in design and look.

```html
<!DOCTYPE html>
<html lang="en">
<head>
<meta charset="utf-8">
<title>Email Signature – Tallgate Consulting</title>
<link rel="stylesheet" href="https://fonts.googleapis.com/css2?family=Questrial&family=Open+Sans:wght@400&display=swap">
<style>
  :root {
    --brand-blue: #1673bf;
    --brand-orange: #ef5a2a;
    --ink: #1d1d1d;
    --ink-soft: #3a3a3a;
    --paper: #ffffff;
    --divider: #f3b9a2;
  }
  html, body {
    margin: 0;
    padding: 0;
    overflow: hidden;
    background: var(--paper);
  }
  .signature {
    position: relative;
    width: 1200px;
    height: 329px;
    background: var(--paper);
    overflow: hidden;
  }
  .brand {
    position: absolute;
    left: 136px;
    top: 82px;
    display: flex;
    align-items: center;
    gap: 18px;
  }
  .brand-dot {
    width: 58px;
    height: 58px;
    border-radius: 50%;
    background: var(--brand-orange);
    flex: none;
  }
  .brand-name {
    font-family: "Questrial", sans-serif;
    color: var(--brand-blue);
    line-height: 0.98;
    margin: 0;
  }
  .brand-name .line-main { display: block; font-size: 66px; letter-spacing: 1px; }
  .brand-name .line-sub { display: block; font-size: 40px; letter-spacing: 3px; }
  .divider {
    position: absolute;
    left: 595px;
    top: 63px;
    width: 2px;
    height: 160px;
    background: linear-gradient(to bottom, rgba(243,185,162,0), var(--divider) 20%, var(--divider) 80%, rgba(243,185,162,0));
  }
  .contact {
    position: absolute;
    left: 654px;
    top: 78px;
  }
  .contact-name {
    font-family: "Questrial", sans-serif;
    font-size: 24px;
    margin: 0 0 22px;
    color: var(--ink);
    white-space: nowrap;
  }
  .contact-name .person { color: var(--brand-blue); }
  .contact-list {
    list-style: none;
    margin: 0;
    padding: 0;
  }
  .contact-item {
    display: flex;
    align-items: center;
    gap: 17px;
    height: 32px;
    margin-bottom: 24px;
    font-family: "Open Sans", sans-serif;
    font-size: 22px;
    color: var(--ink-soft);
    letter-spacing: 0.4px;
  }
  .contact-icon { width: 26px; height: 26px; flex: none; }
  .footer-bands {
    position: absolute;
    left: 0;
    bottom: 0;
    width: 1200px;
    height: 32px;
  }
</style>
</head>
<body>
  <div class="signature">
    <div class="brand">
      <span class="brand-dot"></span>
      <p class="brand-name">
        <span class="line-main">Tallgate</span>
        <span class="line-sub">consulting</span>
      </p>
    </div>

    <div class="divider"></div>

    <div class="contact">
      <p class="contact-name"><span class="person">Sam Harlow,</span> Client Relations</p>
      <ul class="contact-list">
        <li class="contact-item">
          <svg class="contact-icon" viewBox="0 0 26 26" aria-hidden="true">
            <circle cx="13" cy="13" r="11.5" fill="none" stroke="#333" stroke-width="1.4"/>
            <path d="M9.2 7.2c.8-.5 1.5-.3 1.8.3l1 1.9c.3.6.1 1.1-.4 1.4l-.7.4c.4 1.5 1.3 3 2.5 4.1l.7-.4c.5-.3 1.1-.2 1.4.4l1.1 1.8c.3.6.1 1.3-.6 1.7-1.3.8-2.7.5-4-.6-1.8-1.6-3.2-3.9-3.7-6.3-.3-1.8.2-3.2.9-4.7z" fill="#333"/>
          </svg>
          <span>+61400 555 018</span>
        </li>
        <li class="contact-item">
          <svg class="contact-icon" viewBox="0 0 26 26" aria-hidden="true">
            <g fill="none" stroke="#333" stroke-width="1.4">
              <circle cx="13" cy="13" r="11.5"/>
              <ellipse cx="13" cy="13" rx="5" ry="11.5"/>
              <line x1="13" y1="1.5" x2="13" y2="24.5"/>
              <line x1="1.5" y1="13" x2="24.5" y2="13"/>
              <path d="M3.5 7h19M3.5 19h19"/>
            </g>
          </svg>
          <span>tallgate.com.au</span>
        </li>
      </ul>
    </div>

    <svg class="footer-bands" viewBox="0 0 1200 32" preserveAspectRatio="none" aria-hidden="true">
      <polygon points="0,0 570,0 515,32 0,32" fill="var(--brand-orange)"/>
      <polygon points="592,0 1200,0 1200,32 538,32" fill="var(--brand-blue)"/>
    </svg>
  </div>
</body>
</html>
```